Lakemont Hydro Partners, Inc. Company Brochure

I would like someone to design a brochure that can be handed out to prospective clients. We are a full service water and wastewater operations company that provides services to Municipal Utility Districts and citys. I would like something that is catchy to the eye and reflects a company that prides itself on providing personal service to its clients. We need to revamp our website, that's next, but the website does have a description of our company and services offered. You can find that information at www.lakemonthydropartners.example

```html
<!DOCTYPE html>
<html lang="en">
<head>
<meta charset="utf-8">
<title>Lakemont Hydro Partners, Inc. — Company Brochure</title>
<link href="https://fonts.googleapis.com/css2?family=Oxygen:wght@400;700&family=Didact+Gothic&display=swap" rel="stylesheet">
<style>
  :root{
    --stage:#e6e7e9;
    --navy:#1b5fae;
    --sky:#2fa3e6;
    --pale:#cdeefa;
    --pale-2:#e7f7fd;
    --teal:#5fd0e8;
    --teal-deep:#36b6d9;
    --ocean:#1687d9;
    --ocean-deep:#0e6fc0;
    --splash-light:#9fdaf5;
    --splash-mid:#4fb2ea;
    --ink:#1d2a36;
    --white:#ffffff;
  }
  *{margin:0;padding:0;box-sizing:border-box}
  html,body{width:1200px;height:1029px;overflow:hidden}
  body{background:var(--stage);font-family:"Didact Gothic",sans-serif;color:var(--ink);position:relative}

  .brochure{position:absolute;left:60px;top:97px;width:1080px;height:835px;display:flex;box-shadow:0 6px 24px rgba(0,0,0,.18);overflow:hidden}
  .panel{position:relative;width:360px;height:835px;overflow:hidden}

  .panel--about{background:linear-gradient(180deg,var(--pale) 0%,var(--pale-2) 60%,var(--pale) 100%)}
  .panel--services{background:linear-gradient(180deg,var(--teal) 0%,var(--teal-deep) 100%)}
  .panel--mission{background:linear-gradient(180deg,var(--pale-2) 0%,var(--pale) 100%)}

  .photo{position:absolute}
  .photo--ripple{left:0;top:0;width:360px;height:200px;background:radial-gradient(ellipse at 60% 65%,#d9f1fb 0%,#7cc3e6 35%,#2f7fb8 75%,#1c5d92 100%)}
  .photo--glass{left:24px;top:0;width:312px;height:118px;background:radial-gradient(ellipse at 55% 55%,#9fd3f2 0%,#3d8fd0 55%,#e9f4fb 100%)}
  .photo--child{left:40px;top:440px;width:280px;height:250px;border-radius:0 0 0 28px;background:radial-gradient(ellipse at 40% 75%,#cfe7ef 0%,#7aa55a 35%,#3f6b2a 80%)}

  .heading{font-family:"Oxygen",sans-serif;font-weight:400;font-size:26px;letter-spacing:.5px;text-transform:uppercase;color:var(--navy);position:absolute;white-space:nowrap}
  .heading .accent{color:var(--sky)}
  .panel--services .heading .accent{color:var(--white)}

  .heading--about{left:24px;top:215px}
  .heading--services{left:0;right:0;top:40px;text-align:center}
  .heading--mission{left:24px;top:132px}

  .card{position:absolute;background:var(--white)}
  .card--about{left:20px;top:262px;width:320px;height:560px;border-radius:18px 18px 0 0;padding:22px 22px}
  .card--mission{left:20px;top:178px;width:320px;height:530px;border-radius:18px 18px 18px 30px;padding:22px 22px}

  .body-copy{font-size:12.6px;line-height:1.75;color:var(--ink)}
  .body-copy + .body-copy{margin-top:20px}

  .services-box{position:absolute;left:30px;top:92px;width:300px;height:610px;border-radius:20px;background:linear-gradient(180deg,var(--ocean) 0%,var(--ocean-deep) 100%);padding:24px 20px 24px 22px}
  .service-list{list-style:none;color:var(--white);font-size:13.2px;line-height:1.7}
  .service-list li{position:relative;padding-left:14px}
  .service-list li::before{content:"";position:absolute;left:0;top:9px;width:5px;height:5px;border-radius:50%;background:var(--white)}

  .splash-band{position:absolute;left:60px;top:812px;width:1080px;height:120px;background:linear-gradient(180deg,var(--splash-light) 0%,var(--splash-mid) 55%,var(--pale-2) 100%)}
</style>
</head>
<body>
  <main class="brochure">
    <section class="panel panel--about">
      <div class="photo photo--ripple" role="img" aria-label="Photograph of a water droplet rippling on a blue water surface"></div>
      <h2 class="heading heading--about">About <span class="accent">Our Company</span></h2>
      <div class="card card--about">
        <p class="body-copy">Lakemont Hydro Partners, Inc. was incorporated in the state of Texas in 1989. Lakemont Hydro Partners, Inc. is a water and waste water utility operations and billing company.</p>
        <p class="body-copy">All personnel employed by Lakemont Hydro Partners, Inc. are licensed by the State Water Board in water &amp; waste water operations and obtain the proper training needed to successfully operate treatment plants to their maximum capability. We are certified to operate surface water, ground water, and waste water treatment facilities to their maximum capability.</p>
        <p class="body-copy">Here at Lakemont Hydro Partners, Inc., we feel that it is important to provide the highest caliber of services available to the Districts in which we operate. We offer the ability to tailor our services based on the current needs of the District</p>
      </div>
    </section>

    <section class="panel panel--services">
      <h2 class="heading heading--services">Service <span class="accent">Offered</span></h2>
      <div class="services-box">
        <ul class="service-list">
          <li>Surface Water Plant Operations</li>
          <li>Waste Water Plant Operations</li>
          <li>Ground Water Well Operations</li>
          <li>Distribution and Collection System maintenance and repairs</li>
          <li>New Construction Water and Sewer Taps, and all inspections required</li>
          <li>Billing and Collections</li>
          <li>Meter Reading</li>
          <li>Consulting/Management</li>
          <li>Lab Work and Reporting to any and all regulating agencies</li>
          <li>Project Planning</li>
          <li>Assist in Annual Budget Planning</li>
          <li>Smoke Testing</li>
          <li>Park and Trail maintenance</li>
          <li>Detention pond maintenance</li>
        </ul>
      </div>
    </section>

    <section class="panel panel--mission">
      <div class="photo photo--glass" role="img" aria-label="Photograph of water pouring into a clear drinking glass"></div>
      <h2 class="heading heading--mission">Our Mission <span class="accent">&amp; Vision</span></h2>
      <div class="card card--mission">
        <p class="body-copy">Lakemont Hydro Partners, Inc's mission is to produce and deliver potable drinking water and treat residential wastewater in a safe, reliable, efficient, and environmentally sound manner.</p>
        <p class="body-copy">Our vision is to be the recognized performance leader of the water and wastewater utility industry. Being a performance leader means we will achieve operational excellence, industry-leading customer satisfaction and superior financial performance.</p>
      </div>
      <div class="photo photo--child" role="img" aria-label="Photograph of a child drinking from a garden hose outdoors"></div>
    </section>
  </main>

  <div class="splash-band" role="img" aria-label="Illustration of blue water splashes and bubbles along the lower edge"></div>
</body>
</html>
```